Fontenot Bayou Grillhouse (Owners Card)

Need a classy, but modern business card. I have included a promotional card for the steakhouse. I need one for myself (the owner) that is more professional.

Target Market(s)

General Public

Industry/Entity Type

Food service

Contact Information for Business Card

Name, business address, phone number, email, logo

Font styles to use
Serif
Sans Serif
Decorative
Script

Requirements
Must have
• My name (Darvel Pruitt), business address (327 Oakmere Street), phone number (510) 493-2615, email (Dpruittkr4@mailvane.example. On the back of the card: Psalms 27 1 The LORD is my light and my salvation— whom shall I fear? The LORD is the stronghold of my life— of whom shall I be afraid? 2 When the wicked advance against me to devour me, it is my enemies and my foes who will stumble and fall. 3 Though an army besiege me, my heart will not fear; though war break out against me, even then I will be confident.
Nice to have
• Something that’s bold, but modern and professional.

```html
<!DOCTYPE html>
<html lang="en">
<head>
<meta charset="utf-8">
<title>Fontenot Bayou Grillhouse – Owner Card</title>
<link rel="stylesheet" href="https://fonts.googleapis.com/css2?family=Cinzel:wght@700&family=Noto+Serif:wght@400&display=swap">
<style>
  :root {
    --bg: #e7e8ea;
    --ink: #050608;
    --paper: #ffffff;
    --text-dark: #1a1a1a;
    --red: #e52228;
    --orange: #f26522;
    --amber: #f7a823;
    --green: #7cc243;
  }
  html, body {
    margin: 0;
    padding: 0;
    width: 1200px;
    height: 1200px;
    overflow: hidden;
    background: var(--bg);
  }
  .canvas { position: relative; width: 1200px; height: 1200px; }

  .card {
    position: absolute;
    width: 553px;
    height: 315px;
    overflow: hidden;
  }

  /* Back of card */
  .card-back { left: 203px; top: 241px; background: var(--ink); }
  .verse {
    position: absolute;
    left: 100px;
    width: 380px;
    margin: 0;
    text-align: center;
    font-family: "Noto Serif", serif;
    font-size: 15px;
    line-height: 18.3px;
    color: var(--paper);
  }
  .verse-1 { top: 72px; }
  .verse-2 { top: 127px; }
  .verse-3 { top: 182px; }
  .verse-number {
    position: absolute;
    left: 74px;
    width: 21px;
    height: 21px;
    border-radius: 50%;
    font-family: "Noto Serif", serif;
    font-size: 13px;
    line-height: 21px;
    text-align: center;
    color: var(--ink);
  }
  .num-1 { top: 73px; background: linear-gradient(180deg, var(--orange), var(--green)); }
  .num-2 { top: 128px; background: linear-gradient(180deg, var(--orange), var(--amber)); }
  .num-3 { top: 183px; background: linear-gradient(180deg, var(--red), var(--amber)); }

  /* Front of card */
  .card-front { left: 390px; top: 633px; background: var(--paper); }
  .front-art { position: absolute; left: 0; top: 0; }
  .brand-name {
    position: absolute;
    left: 14px;
    width: 216px;
    top: 140px;
    text-align: center;
    font-family: "Cinzel", serif;
    font-weight: 700;
    font-size: 17px;
    line-height: 22px;
    color: var(--amber);
  }
  .owner-name {
    position: absolute;
    left: 300px;
    top: 70px;
    margin: 0;
    font-family: "Cinzel", serif;
    font-weight: 700;
    font-size: 25px;
    letter-spacing: 1px;
    color: var(--red);
  }
  .contact-list {
    position: absolute;
    left: 292px;
    top: 0;
    margin: 0;
    padding: 0;
    list-style: none;
    font-family: "Noto Serif", serif;
    font-size: 16px;
    color: var(--text-dark);
  }
  .contact-list li { position: absolute; white-space: nowrap; line-height: 20px; }
  .contact-phone { top: 160px; }
  .contact-email { top: 195px; }
  .contact-address { top: 226px; }
  .edge-tab {
    position: absolute;
    left: 544px;
    top: 60px;
    width: 9px;
    height: 45px;
    border-radius: 6px 0 0 6px;
    background: var(--red);
  }
</style>
</head>
<body>
<div class="canvas">

  <section class="card card-back" aria-label="Card back">
    <span class="verse-number num-1">1</span>
    <p class="verse verse-1">Psalms 27 1 The LORD is my light and my salvation—<br>whom shall I fear? The LORD is the stronghold of<br>my life— of whom shall I be afraid?</p>
    <span class="verse-number num-2">2</span>
    <p class="verse verse-2">When the wicked advance against me to devour me,<br>it is my enemies and my foes who will<br>stumble and fall.</p>
    <span class="verse-number num-3">3</span>
    <p class="verse verse-3">Though an army besiege me, my heart will not fear;<br>though war break out against me, even<br>then I will be confident.</p>
  </section>

  <section class="card card-front" aria-label="Card front">
    <svg class="front-art" width="553" height="315" viewBox="0 0 553 315">
      <defs>
        <linearGradient id="accent-strip" x1="0" y1="0" x2="0" y2="1">
          <stop offset="0" stop-color="#f26522"/>
          <stop offset="0.5" stop-color="#f7a823"/>
          <stop offset="1" stop-color="#7cc243"/>
        </linearGradient>
      </defs>
      <path d="M244 126 L276 142 L276 265 A50 50 0 0 1 226 315 L190 315 Z" fill="url(#accent-strip)"/>
      <path d="M0 0 H244 V265 A50 50 0 0 1 194 315 H0 Z" fill="#050608"/>
      <g class="contact-icons">
        <circle cx="260" cy="171" r="11" fill="#ffffff"/>
        <path d="M255.5 165.5 c1-1 2-1 2.5 0 l1.2 2 c.4.8 0 1.4-.6 1.8 c.8 1.8 2 3 3.8 3.8 c.4-.6 1-1 1.8-.6 l2 1.2 c1 .5 1 1.5 0 2.5 c-1.5 1.5-4 1-7-1.8 c-3-3-3.6-5.6-3.7-8.9z" fill="#f26522"/>
        <circle cx="260" cy="206" r="11" fill="#ffffff"/>
        <rect x="253.5" y="201.5" width="13" height="9" rx="1" fill="none" stroke="#f47a20" stroke-width="1.5"/>
        <path d="M253.5 202 L260 207 L266.5 202" fill="none" stroke="#f47a20" stroke-width="1.5"/>
        <circle cx="260" cy="237" r="11" fill="#ffffff"/>
        <path d="M260 244 C256 239 255.5 236.8 255.5 235 A4.5 4.5 0 0 1 264.5 235 C264.5 236.8 264 239 260 244 Z" fill="none" stroke="#f7a823" stroke-width="1.5"/>
        <circle cx="260" cy="235" r="1.5" fill="#f7a823"/>
      </g>
    </svg>
    <div class="brand-name">Fontenot Bayou<br>Grillhouse</div>
    <h1 class="owner-name">DARVEL PRUITT</h1>
    <ul class="contact-list">
      <li class="contact-phone">(510) 493-2615</li>
      <li class="contact-email">Dpruittkr4@mailvane.example</li>
      <li class="contact-address">327 Oakmere Street</li>
    </ul>
    <span class="edge-tab"></span>
  </section>

</div>
</body>
</html>
```